Web Design Project - Vextrion

We have created an initial website at http://www.vextrion-example.com

This project requires you to take the current website and redesigning it to improve the overall look and feel.

Feel free to experiment with everything including:

~ colour schemes
~ layout

The only constraints are

- the text content
- the app icons on /games
- the logo structure (feel free to change the colour schemes / logo image)

In terms of process - please feel free to post concepts / mockups for one page - if this is easier for you to do quickly (without revamping the entire site).

As well as the website, please provide designs for a facebook page cover and profile picture for http://www.socialpage-example.com/pages/Vextrion/730194652018364

Thanks for the submissions - but we've not quite found what we're looking for.

This site is on which appeals to us - please use this for inspiration: http://brambury-example.com/

Thanks

Reason: I am about to make this project "guaranteed" and want to give more time to submit

Please submit your creative ideas - we look forward to receiving them.

Reason: Hi, Deadline extended so that we can see revisions Thanks

Target Market(s)

Marketing Executives / CEOs of Media Companies

Industry/Entity Type

Games

```html
<!DOCTYPE html>
<html lang="en">
<head>
<meta charset="utf-8">
<title>Vextrion – In-Play Second Screen Games</title>
<link href="https://fonts.googleapis.com/css2?family=Bebas+Neue&family=Quicksand:wght@500&family=Arimo:wght@400;700&display=swap" rel="stylesheet">
<style>
:root{
  --teal:#2aa6c4;
  --teal-dark:#1a8aa8;
  --teal-light:#41c0dd;
  --green:#8cc63f;
  --green-dark:#6ca52a;
  --orange:#f7792a;
  --navy:#1d3f73;
  --grey-bg:#e1e5e8;
  --text:#333;
  --heading:#333;
  --white:#fff;
  --hero-top:#cfe6f5;
}
*{margin:0;padding:0;box-sizing:border-box}
html,body{width:1200px;height:1168px;overflow:hidden}
body{position:relative;background:var(--white);font-family:"Arimo",Arial,sans-serif;color:var(--text)}

.topline{position:absolute;left:0;top:0;width:1200px;height:3px;background:#999}
.header{position:absolute;left:0;top:3px;width:1200px;height:145px;background:var(--white)}

.brand{position:absolute;left:252px;top:52px;display:flex;align-items:center;gap:10px;font-family:"Arimo",Arial,sans-serif;font-weight:700;font-size:30px;color:var(--orange)}
.brand-mark{width:26px;height:26px;background:var(--navy)}

.social{position:absolute;left:878px;top:12px;display:flex;gap:3px}
.social span{width:21px;height:21px;border-radius:2px;background:var(--navy)}
.social span:nth-child(2){background:var(--teal-light)}
.social span:nth-child(3){background:#3b7ac6}
.social span:nth-child(4){background:#1e6fa3}
.social span:nth-child(5){background:#222}

.main-nav{position:absolute;left:494px;top:81px;width:508px;height:47px;border-radius:24px;background:linear-gradient(#fff,#e8eaec);border:1px solid #c9ccd0;box-shadow:0 3px 5px rgba(0,0,0,.18);display:flex;align-items:center;padding-left:44px}
.main-nav a{font-weight:700;font-size:12.5px;color:#222;text-decoration:none;height:100%;display:flex;align-items:center;padding:0 16px}
.main-nav a.active{background:#b9dde6;color:#1e4d60;padding:0 20px;margin-right:6px}

.tagline{position:absolute;left:0;top:148px;width:1200px;height:54px;background:var(--teal);display:flex;align-items:center;justify-content:center;font-family:"Bebas Neue",Impact,sans-serif;font-size:33px;letter-spacing:.5px;color:var(--white)}

.hero{position:absolute;left:0;top:202px;width:1200px;height:452px;background:linear-gradient(var(--hero-top),#f4f8fb 55%,#fff)}
.hero-divider{position:absolute;left:598px;top:0;width:4px;height:452px;background:linear-gradient(90deg,rgba(0,0,0,.07),rgba(0,0,0,0))}

.bubble{position:absolute;top:31px;width:382px;height:102px;border:3px solid var(--white);border-radius:48px;box-shadow:0 2px 5px rgba(0,0,0,.25);display:flex;align-items:center;justify-content:center;text-align:center;font-family:"Quicksand",sans-serif;font-weight:500;font-size:17px;line-height:21px;color:#102a35;padding:0 14px}
.bubble::after{content:"";position:absolute;left:50%;bottom:-13px;margin-left:-10px;border:10px solid transparent;border-top:12px solid;border-bottom:0}
.bubble-games{left:205px;background:linear-gradient(var(--teal-light),var(--teal-dark))}
.bubble-games::after{border-top-color:var(--teal-dark)}
.bubble-screens{left:610px;background:linear-gradient(#9fd24f,var(--green-dark))}
.bubble-screens::after{border-top-color:var(--green-dark)}

.mascot{position:absolute;top:155px;height:300px;border-radius:40px 40px 20px 20px}
.mascot-games{left:228px;width:285px;background:radial-gradient(ellipse at 50% 45%,#3cb7d8 0 28%,#21507f 29% 40%,rgba(33,80,127,.15) 41%,rgba(255,255,255,0) 70%)}
.mascot-screens{left:620px;width:335px;background:radial-gradient(ellipse at 50% 45%,#8cc63f 0 26%,var(--orange) 27% 38%,rgba(247,121,42,.15) 39%,rgba(255,255,255,0) 70%)}

.zigzag{position:absolute;left:0;top:652px;width:1200px;height:22px;background:
  linear-gradient(135deg,var(--orange) 50%,transparent 50%) 0 8px/10px 10px repeat-x,
  linear-gradient(225deg,var(--orange) 50%,transparent 50%) 0 8px/10px 10px repeat-x,
  linear-gradient(var(--orange),var(--orange)) 0 0/100% 10px no-repeat,
  var(--grey-bg)}

.audience{position:absolute;left:0;top:674px;width:1200px;height:408px;background:var(--grey-bg)}
.audience-heading{position:absolute;top:25px;width:400px;text-align:center;font-family:"Bebas Neue",Impact,sans-serif;font-weight:400;font-size:27px;line-height:31px;color:var(--heading)}
.heading-owners{left:187px}
.heading-players{left:582px}

.panel{position:absolute;top:115px;width:388px;height:223px;background:linear-gradient(#fafbfc,#e9edf0);border:1px solid #fff;border-radius:6px;box-shadow:0 2px 6px rgba(0,0,0,.22);padding:12px 20px 0 31px;clip-path:polygon(0 0,100% 0,100% 100%,0 88%)}
.panel-owners{left:205px}
.panel-players{left:607px;clip-path:polygon(0 0,100% 0,100% 88%,0 100%)}
.panel ul{list-style:none}
.panel li{position:relative;font-size:11.8px;line-height:20.5px;text-align:justify}
.panel li::before{content:"";position:absolute;left:-16px;top:6px;border-left:7px solid #5a8fb6;border-top:4px solid transparent;border-bottom:4px solid transparent}
.panel a{color:var(--orange);font-weight:700;text-decoration:none}
.more{position:absolute;width:36px;height:36px;border-radius:50%;background:#2b2b2b;display:flex;align-items:center;justify-content:center}
.panel-owners .more{right:10px;bottom:12px}
.panel-players .more{right:12px;bottom:36px}
.more svg{width:16px;height:16px}

.footer-tab{position:absolute;left:353px;top:1053px;width:487px;height:30px;background:var(--navy);clip-path:polygon(5% 0,95% 0,100% 100%,0 100%)}
.footer-band{position:absolute;left:0;top:1081px;width:1200px;height:37px;background:var(--navy)}
.footer-nav{position:absolute;left:353px;top:1075px;width:487px;display:flex;justify-content:center;align-items:center;gap:14px;font-size:12.5px;color:var(--white)}
.footer-nav a{color:var(--white);text-decoration:none}
.footer-nav a.active{color:var(--teal-light)}
.legal{position:absolute;left:0;top:1118px;width:1200px;height:50px;background:var(--teal);color:var(--white);font-size:11px;line-height:17px;text-align:center;padding-top:7px}
</style>
</head>
<body>
<div class="topline"></div>
<header class="header">
  <div class="brand"><span class="brand-mark"></span>Vextrion</div>
  <div class="social" aria-label="Social links"><span></span><span></span><span></span><span></span><span></span></div>
  <nav class="main-nav">
    <a class="active" href="#">Home</a><a href="#">About</a><a href="#">Games</a><a href="#">Solutions</a><a href="#">Updates</a><a href="#">Contact</a>
  </nav>
</header>

<div class="tagline">"Delivering in-play second screen games based on live broadcast events"</div>

<section class="hero">
  <div class="hero-divider"></div>
  <p class="bubble bubble-games">In-Play Games allow players to interact with real-time scoring whilst watching live events with instant scoring.</p>
  <p class="bubble bubble-screens">Second-Screens are mobile phones or tablets used by viewers to enrich their TV watching experience.</p>
  <div class="mascot mascot-games" role="img" aria-label="Illustration of a blue TV-headed mascot holding a microphone and bat, standing on a football"></div>
  <div class="mascot mascot-screens" role="img" aria-label="Illustration of an orange TV-headed mascot holding two tablets, standing on a football"></div>
</section>

<div class="zigzag"></div>

<section class="audience">
  <h2 class="audience-heading heading-owners">For media owners, broadcasters or<br>sponsors of live events</h2>
  <h2 class="audience-heading heading-players">Inplay for<br>for game players and fans</h2>

  <div class="panel panel-owners">
    <ul>
      <li>Games can be re-skinned &amp; launched for your live event</li>
      <li>Increases value of live media rights through increased viewer engagement</li>
      <li>Games capture extensive customer data to enhance your CRM capabilities</li>
      <li>Deep social network integration and social gameplay mechanisms maximise chances of the game "going viral"</li>
      <li><a href="#">Click here</a> to find out more about our Solutions</li>
    </ul>
    <span class="more"><svg viewBox="0 0 16 16"><path d="M8 2v12M2 8h12" stroke="#2aa6c4" stroke-width="3"/></svg></span>
  </div>

  <div class="panel panel-players">
    <ul>
      <li>Play games with friends while watching live events</li>
      <li>Real-time gameplay based on the event you're watching</li>
      <li>Compete against your friends and other players</li>
      <li>Free to play prizes for the best performing games</li>
      <li><a href="#">Click here</a> to see a list of our games</li>
    </ul>
    <span class="more"><svg viewBox="0 0 16 16"><path d="M8 2v12M2 8h12" stroke="#8cc63f" stroke-width="3"/></svg></span>
  </div>
</section>

<div class="footer-tab"></div>
<div class="footer-band"></div>
<nav class="footer-nav">
  <a class="active" href="#">Home</a><span>/</span><a href="#">About</a><span>/</span><a href="#">Games</a><span>/</span><a href="#">Solutions</a><span>/</span><a href="#">Updates</a><span>/</span><a href="#">Contact</a>
</nav>
<footer class="legal">
  Use of this Web site constitutes acceptance of Vextrion's Terms of Service and Privacy Policy<br>
  © Copyright 2012 Halvern Systems Ltd. All rights reserved.
</footer>
</body>
</html>
```